New web design for a service provider in the medical field

We are looking for a new design for our website. We are a company that repairs and sells medical endoscopes. Our customers include doctors and hospitals. Our current website can be found at https://lumenfix.example/en/lumenfix-english.
We need a new web design (without programming) for the following 3 pages:
-Startpage https://lumenfix.example/en/lumenfix-english/
-Used endoscopes https://lumenfix.example/en/used-endoscopes/
-Purchase https://lumenfix.example/en/purchase/
The design should be modern and stylish.
The blue color of the logo should be reflected on the page, but not too intrusive.
I have uploaded the images from the header. If more images are needed, let me know and I will upload them.

Target Market(s)
Doctors and hospitals

```html
<!DOCTYPE html>
<html lang="en">
<head>
<meta charset="utf-8">
<title>LumenFix – Endoscope Repair</title>
<link href="https://fonts.googleapis.com/css2?family=Poppins:wght@300;400;500;600&display=swap" rel="stylesheet">
<style>
:root{
  --blue:#2aa3dc;
  --navy:#24394b;
  --ink:#2b2b2b;
  --muted:#5f6468;
  --grey:#e4e4e4;
  --band:#cfcfcf;
  --card:#efefef;
  --sky:#a8d4e8;
  --footer:#3f86b0;
  --white:#fff;
}
*{box-sizing:border-box;margin:0;padding:0}
html,body{width:1200px;height:3383px;overflow:hidden}
body{font-family:"Poppins",sans-serif;color:var(--ink);background:var(--white);position:relative}
section,header,footer{position:relative;width:1200px;overflow:hidden}
.abs{position:absolute}
a{color:inherit;text-decoration:none}
.btn{display:flex;align-items:center;justify-content:center;background:var(--navy);color:var(--white);font-size:13px;border-radius:2px}

/* header */
.site-header{height:122px;background:var(--white)}
.brand{left:195px;top:40px;display:flex;align-items:center;gap:10px;font-size:22px;font-weight:600;color:var(--navy)}
.brand i{width:14px;height:14px;border-radius:50%;background:var(--blue)}
.topbar{left:446px;top:27px;display:flex;gap:16px;font-size:10.5px;color:var(--ink);align-items:center}
.topbar span{display:flex;align-items:center;gap:4px}
.topbar svg{width:10px;height:10px;fill:var(--blue)}
.lang{font-weight:600;margin-left:8px}.lang em{font-style:normal;color:var(--blue);font-weight:400}
.mainnav{left:411px;top:66px;display:flex;gap:18px;font-size:11px;font-weight:500;color:var(--navy)}
.nav-purchase{left:929px;top:59px;width:72px;height:32px;font-size:11px;font-weight:500}

/* hero */
.hero{height:435px}
.hero-photo{inset:0;background:radial-gradient(ellipse at 70% 30%,#8a8d90,#55595d 55%,#3d4043)}
.hero-title{width:100%;top:90px;text-align:center;color:var(--white);font-weight:300;font-size:39px;letter-spacing:3px;line-height:57px}
.hero-tag{left:516px;top:232px;width:194px;height:56px;border:2px solid var(--white);color:var(--white);display:flex;align-items:center;justify-content:center;font-weight:600;font-size:15px}
.hero-lead{width:100%;top:312px;text-align:center;color:var(--white);font-size:15px;line-height:26px;letter-spacing:1px}

/* intro */
.intro{height:471px;background:var(--grey)}
.intro-photo{left:194px;top:73px;width:367px;height:323px;background:linear-gradient(135deg,#e9ecee,#9aa1a6 55%,#c8b89e)}
.intro-title{left:594px;top:76px;width:420px;font-size:22.5px;font-weight:300;line-height:35px;color:var(--ink)}
.intro-copy{left:597px;top:196px;width:400px;font-size:13px;line-height:21px;color:var(--muted)}
.intro-copy p+p{margin-top:21px}
.intro-copy b{color:var(--blue);font-weight:400}

/* makers */
.makers{height:129px;background:var(--band)}
.maker{top:25px;height:77px;background:var(--white);display:flex;align-items:center;justify-content:center;font-weight:600;font-size:22px;color:var(--navy)}

/* services */
.services{height:420px;background:var(--grey)}
.card{background:var(--card);box-shadow:0 2px 10px rgba(0,0,0,.12);padding:26px 38px}
.card.raised{background:var(--white);z-index:2;box-shadow:0 4px 16px rgba(0,0,0,.15)}
.card h3{display:flex;align-items:center;gap:14px;font-size:29px;font-weight:300;color:var(--blue)}
.card h3 svg{width:40px;height:40px;fill:var(--blue)}
.card h4{font-size:15.5px;font-weight:400;margin:20px 0 22px}
.card p{font-size:12.8px;line-height:22px;color:var(--muted)}
.card p a{color:var(--blue);text-decoration:underline}

/* pickup */
.pickup{height:331px}
.pickup-bg{inset:0;background:linear-gradient(90deg,#c9d3d6,#dfe3e4 45%,#b3b3b3 70%,#6b6b6b)}
.pickup-box{left:400px;top:45px;width:396px;height:241px;background:var(--white);text-align:center;box-shadow:0 2px 10px rgba(0,0,0,.1)}
.pickup-box h2{margin-top:64px;font-size:26px;font-weight:300;color:var(--navy)}
.pickup-box p{margin-top:6px;font-size:13px;color:var(--navy)}
.pickup-box .btn{width:146px;height:41px;margin:32px auto 0;font-size:13px}

/* values */
.values{height:633px;background:radial-gradient(ellipse 300px 310px at 617px 320px,#fff 0%,#e8f4fa 35%,var(--sky) 100%)}
.value{width:160px;margin-left:-80px;text-align:center;color:var(--navy)}
.value svg{width:30px;height:30px;fill:var(--white);display:block;margin:0 auto 8px}
.value h5{font-size:15px;font-weight:500;line-height:19px;letter-spacing:.5px}
.value p{font-size:11.5px;line-height:13.5px;margin-top:5px}
.motto{left:467px;top:260px;width:300px;text-align:center;font-size:25px;letter-spacing:3px;line-height:38px;color:var(--blue);font-weight:400}
.motto u{text-underline-offset:6px}

/* reasons */
.reasons{height:650px;background:var(--white)}
.reasons h2{position:absolute;top:56px;width:100%;text-align:center;font-size:29px;font-weight:300;color:var(--navy)}
.reason{width:380px}
.reason h4{display:flex;align-items:center;gap:10px;font-size:17.5px;font-weight:300;color:var(--navy)}
.reason h4 svg{width:26px;height:26px;fill:var(--blue);flex:none}
.reason p{margin:6px 0 0 40px;font-size:10px;line-height:16px;color:var(--ink)}
.reasons .btn{left:471px;top:538px;width:259px;height:41px;font-size:13px}

/* footer */
.site-footer{height:192px;background:linear-gradient(180deg,var(--footer),#5a9dc2)}
.footer-brand{left:207px;top:0;width:173px;height:96px;background:var(--white);display:flex;align-items:center;justify-content:center;gap:8px;font-size:19px;font-weight:600;color:var(--navy)}
.footer-brand i{width:11px;height:11px;border-radius:50%;background:var(--blue)}
.social{top:127px;width:18px;height:18px;border-radius:50%;background:var(--navy)}
.copy{left:212px;top:165px;font-size:8px;color:var(--white)}
.fcol{top:38px;color:var(--white);font-size:9px;line-height:15px}
.fcol h6{font-size:10.5px;font-weight:600;margin-bottom:6px}
</style>
</head>
<body>

<header class="site-header">
  <a class="brand abs" href="https://lumenfix.example/en/lumenfix-english/"><i></i>LumenFix</a>
  <div class="topbar abs">
    <span><svg viewBox="0 0 10 10"><circle cx="5" cy="5" r="5"/></svg>pick-up order</span>
    <span><svg viewBox="0 0 10 10"><circle cx="3" cy="3" r="2"/><circle cx="7" cy="3" r="2"/><rect x="0" y="6" width="10" height="4" rx="2"/></svg>about us</span>
    <span><svg viewBox="0 0 10 10"><rect y="2" width="10" height="7"/></svg>contact us</span>
    <span>info@lumenfix.example</span>
    <span style="margin-left:8px"><svg viewBox="0 0 10 10"><path d="M1 1l3 0 1 3-2 1c1 2 2 3 3 3l1-2 3 1v3C4 10 0 6 1 1z"/></svg>+49 4000 555 0100</span>
    <span class="lang">DE /&nbsp;<em>EN</em></span>
  </div>
  <nav class="mainnav abs">
    <a>Endoscope Repair</a><a>Used Endoscopes ⌄</a><a>Endoscopy Systems</a><a>Endoscopy Accessories ⌄</a>
  </nav>
  <a class="btn nav-purchase abs" href="https://lumenfix.example/en/purchase/">Purchase</a>
</header>

<section class="hero">
  <div class="hero-photo abs" role="img" aria-label="Close-up photo of a flexible endoscope control body"></div>
  <h1 class="hero-title abs">PUT YOUR ENDOSCOPE<br>IN RELIABLE HANDS!</h1>
  <div class="hero-tag">LumenFix GmbH</div>
  <p class="hero-lead abs">Specialised in the repair and sale of Aldoris, Penmark and Kiyomi flexible medical endoscopes.<br>As a service-oriented company, we are at your side with our knowledge and skills!</p>
</section>

<section class="intro">
  <div class="intro-photo abs" role="img" aria-label="Photo of an endoscope handle with control wheels"></div>
  <h2 class="intro-title abs">Endoscope repairs and second hand endoscopes from LumenFix – cause the outcome matters!</h2>
  <div class="intro-copy abs">
    <p><b>LumenFix</b> is a privileged partner for the start-up facility or optimisation of existing healthcare facilities, doctor's offices and hospitals. The quality and reliability of our products and our offered service are our best advertisement!</p>
    <p>As a result of optimised processes and highly qualified specialists in our company, we can work very quickly and with high quality for your benefit of least possible restrictions in your doctor's office or in your hospital.</p>
  </div>
</section>

<section class="makers">
  <div class="maker abs" style="left:316px;width:191px">Aldoris</div>
  <div class="maker abs" style="left:540px;width:138px">Penmark</div>
  <div class="maker abs" style="left:707px;width:174px">Kiyomi</div>
</section>

<section class="services">
  <article class="card abs" style="left:56px;top:79px;width:362px;height:269px">
    <h3><svg viewBox="0 0 24 24"><path d="M3 19l9-9-2-2 3-3 6 6-3 3-2-2-9 9zM14 3l2 2-3 3-2-2z M19 14l3 3-3 3-3-3z"/></svg>Repair</h3>
    <h4>Endoscope repair service</h4>
    <p>Manufacturer-independent we repair and maintain endoscopes, individual components (e.g. processors or light sources), accessories and peripherals of the manufacturers Aldoris, Penmark and Kiyomi.</p>
  </article>
  <article class="card raised abs" style="left:418px;top:66px;width:343px;height:293px;padding-top:36px">
    <h3><svg viewBox="0 0 24 24"><circle cx="8" cy="7" r="4"/><circle cx="17" cy="8" r="3.5"/><path d="M0 21c0-5 4-8 8-8s8 3 8 8zM15 21c0-3-1-5-2-6 1-1 3-1 4-1 4 0 7 3 7 7z"/></svg>Sale</h3>
    <h4>Used endoscopes</h4>
    <p>Our regular stock includes refurbished gastroscopes, coloscopes, bronchoscopes, cystoscopes and duodenoscopes from the well-known manufacturers Aldoris, Penmark and Kiyomi.</p>
  </article>
  <article class="card abs" style="left:761px;top:79px;width:383px;height:269px;padding-left:52px">
    <h3><svg viewBox="0 0 24 24"><path d="M0 5h24v14H0zM2 7v10h20V7z"/><circle cx="12" cy="12" r="3.5"/></svg>Purchase</h3>
    <h4>Used endoscopes</h4>
    <p>We are very interested in buying your old endoscopes – even defective and dismantled! We offer fair conditions! Please <a>contact us</a> for a purchase offer!</p>
  </article>
</section>

<section class="pickup">
  <div class="pickup-bg abs" role="img" aria-label="Soft background image with a DNA strand and network lines"></div>
  <div class="pickup-box abs">
    <h2>FAULTY ENDOSCOPE?</h2>
    <p>We ensure quick and smooth repairs!</p>
    <a class="btn">pick-up order</a>
  </div>
</section>

<section class="values">
  <div class="value abs" style="left:511px;top:68px">
    <svg viewBox="0 0 24 24"><circle cx="12" cy="7" r="4"/><circle cx="4" cy="9" r="3"/><circle cx="20" cy="9" r="3"/><path d="M4 20c0-5 4-7 8-7s8 2 8 7zM0 19c0-3 2-5 4-5 1 0 2 0 2 1-2 1-3 3-3 4zM24 19c0-3-2-5-4-5-1 0-2 0-2 1 2 1 3 3 3 4z"/></svg>
    <h5>EXPERIENCE CHARACTERISES US</h5><p>Our team has many years of experience in the business field!</p>
  </div>
  <div class="value abs" style="left:706px;top:68px">
    <svg viewBox="0 0 24 24"><path d="M12 22L2 12C-1 8 2 2 7 3c2 0 4 2 5 3 1-1 3-3 5-3 5-1 8 5 5 9z"/></svg>
    <h5>THE PRODUCT IS CLOSE TO OUR HEARTS</h5><p>We repair and sell second hand, flexible endoscopes!</p>
  </div>
  <div class="value abs" style="left:407px;top:234px">
    <svg viewBox="0 0 24 24"><path d="M8 5l5-4h3v20h-5V7l-3 2z"/></svg>
    <h5>ONE COMPANY FOR EVERYONE</h5><p>We are a service provider for doctors and hospitals!</p>
  </div>
  <div class="value abs" style="left:819px;top:228px">
    <svg viewBox="0 0 24 24"><path d="M2 10h5v12H2zM9 10l4-8c2 0 3 1 3 3l-1 4h6c2 0 3 2 2 4l-2 7c0 1-1 2-3 2H9z"/></svg>
    <h5>GUARANTEED SERVICE</h5><p>You receive a six-month warranty on all repairs!</p>
  </div>
  <div class="motto abs"><u>CAUSE</u><br>THE OUTCOME<br>MATTERS!</div>
  <div class="value abs" style="left:502px;top:410px">
    <svg viewBox="0 0 24 24"><path d="M23 1L1 11l7 3 12-9-9 11v7l4-5 5 3z"/></svg>
    <h5>SERVICES FOR EVERYONE</h5><p>Our service includes the manufacturers Aldoris, Penmark and Kiyomi!</p>
  </div>
  <div class="value abs" style="left:711px;top:410px">
    <svg viewBox="0 0 24 24"><path d="M6 2h12v7a6 6 0 0 1-12 0zM2 3h4v2H4c0 3 1 4 2 5v2c-3-1-4-4-4-9zM22 3h-4v2h2c0 3-1 4-2 5v2c3-1 4-4 4-9zM10 15h4v4h3v3H7v-3h3z"/></svg>
    <h5>QUALITY NOT QUANTITY</h5><p>Reliability and durability instead of inferior replacements!</p>
  </div>
</section>

<section class="reasons">
  <h2>LumenFix GmbH, your decision for your future</h2>
  <div class="reason abs" style="left:215px;top:164px">
    <h4><svg viewBox="0 0 24 24"><path d="M14 1L5 14h6l-2 9 10-14h-6z"/></svg>Fast repairs</h4>
    <p>Keep potential disruptions in your doctor's office or in your hospital at minimum as a result of optimized processes and highly qualified specialists in our company</p>
  </div>
  <div class="reason abs" style="left:622px;top:164px">
    <h4><svg viewBox="0 0 24 24"><path d="M0 16h4v7H0zM5 16c3 0 5 0 7 1h4c1 0 1 2 0 2h-5v1h6l6-3c1 0 2 1 1 2l-7 4H5zM13 1h2v2c2 0 3 1 3 2h-2c0-1-4-1-4 0s1 1 3 2c3 0 4 2 3 4-1 1-2 1-3 1v2h-2v-2c-2 0-3-1-3-3h2c0 1 4 1 4 0s-2-1-3-1c-3-1-4-2-3-4 0-1 1-2 3-2z"/></svg>Highly cost efficient</h4>
    <p>Benefit from our first class recommendations and implementation by our experienced staff. Our goals is to find the best solutions together with you at the best lowest price point.</p>
  </div>
  <div class="reason abs" style="left:215px;top:280px">
    <h4><svg viewBox="0 0 24 24"><path d="M12 2l12 10h-3v10h-6v-7H9v7H3V12H0z"/></svg>On-site service</h4>
    <p>We will gladly pay you a visit to to carry out analysis and repairs on site. Due to our many years of experience – it doesn't get any faster (within a 250 km range)</p>
  </div>
  <div class="reason abs" style="left:622px;top:280px">
    <h4><svg viewBox="0 0 24 24"><path d="M2 10h5v12H2zM9 10l4-8c2 0 3 1 3 3l-1 4h6c2 0 3 2 2 4l-2 7c0 1-1 2-3 2H9z"/></svg>Loan equipment service</h4>
    <p>Use our service of high-quality loan devices during the downtime of your defective endoscope (limited to stock)</p>
  </div>
  <div class="reason abs" style="left:215px;top:398px">
    <h4><svg viewBox="0 0 24 24"><path d="M2 13l3-3 5 5L20 4l3 3-13 13z"/></svg>Without a maintenance contract</h4>
    <p>No subscription or other maintenance contract, but one-time and sustainable repair work</p>
  </div>
  <div class="reason abs" style="left:622px;top:398px">
    <h4><svg viewBox="0 0 24 24"><path d="M12 1a7 7 0 1 1 0 14a7 7 0 0 1 0-14zm0 3a4 4 0 1 0 0 8a4 4 0 0 0 0-8zM7 14l-2 9 4-2 3 3 1-8zM17 14l2 9-4-2-3 3-1-8z"/></svg>First class service</h4>
    <p>Our clients always come first!</p>
  </div>
  <a class="btn abs" href="https://lumenfix.example/en/lumenfix-english/">Learn more about LumenFix!</a>
</section>

<footer class="site-footer">
  <div class="footer-brand abs"><i></i>LumenFix</div>
  <span class="social abs" style="left:213px"></span>
  <span class="social abs" style="left:238px"></span>
  <p class="copy abs">© 2022 LumenFix GmbH</p>
  <div class="fcol abs" style="left:455px"><h6>Navigate</h6>Home<br>Endoscope Repair<br><a href="https://lumenfix.example/en/used-endoscopes/">Used Endoscopes</a><br>Endoscopy Systems<br>Endoscopy Accessories<br><a href="https://lumenfix.example/en/purchase/">Purchase</a></div>
  <div class="fcol abs" style="left:604px"><h6>Support</h6>Help Center<br>FAQ</div>
  <div class="fcol abs" style="left:737px"><h6>Get in touch</h6>LumenFix GmbH<br><br>Lindenweg 12<br>20095 Hafenstadt<br>Germany</div>
  <div class="fcol abs" style="left:898px"><h6>Legal</h6>Terms of Business<br>Terms of Service<br>Privacy Policy<br>Cookie Policy<br>Your Cookie Consent<br>Data Security<br>Whitepaper</div>
</footer>

</body>
</html>
```